Wordpress website for Dance Studio

Hi there, I am looking for Wordpress Website for dance studio. Happy for designed to use available themes. Would like a few pages setup and I can do the rest.

Other things I would like included in this theme :

Nice images page OR moving banner
Blog
Ability for youtubes

Other than that, simple requirements, just a gorgeous looking landing page/site etc.

Target Market(s)

Dance mums and kids (dancers)

Industry/Entity Type

Dance and Performancer

Coding

Coded - Design and coding required

Number of Pages Required

4 page

Font styles to use
Sans Serif

Colors
EB3D1F
EC4F4E
F09395
F8D3D4
FCEDEE

Requirements
Must have
• Wordpress theme
Nice to have
• Artistic, graphical, dance studio theme

```html
<!DOCTYPE html>
<html lang="en">
<head>
<meta charset="utf-8">
<title>Studio Pirouette</title>
<link rel="stylesheet" href="https://fonts.googleapis.com/css2?family=Poppins:wght@400;500;600&family=Open+Sans:wght@400;600&display=swap">
<style>
:root{
  --red:#EB3D1F;
  --coral:#EC4F4E;
  --pink:#F09395;
  --blush:#F8D3D4;
  --mist:#FCEDEE;
  --ink:#111111;
  --text:#333333;
  --muted:#777777;
  --grey:#eeeeee;
  --white:#ffffff;
}
*{margin:0;padding:0;box-sizing:border-box}
html,body{width:1200px;height:3868px;overflow:hidden;background:var(--white)}
body{font-family:"Open Sans",sans-serif;color:var(--text);position:relative}
h1,h2,h3,h4,.brand,.btn,.nav a{font-family:"Poppins",sans-serif}
.abs{position:absolute}
.photo{display:block}

/* hero */
.hero{position:absolute;left:0;top:0;width:1200px;height:725px;
  background:linear-gradient(100deg,#7a6152 0%,#a58c78 35%,#8c7565 60%,#b9a594 100%)}
.hero-shade{position:absolute;inset:0;background:linear-gradient(90deg,rgba(40,25,20,.45),rgba(40,25,20,.05) 60%)}
.brand{position:absolute;left:111px;top:18px;color:var(--white);font-size:27px;font-weight:600}
.nav{position:absolute;top:27px;left:0;width:1200px}
.nav a{position:absolute;color:var(--white);font-size:15px;text-decoration:none;letter-spacing:.5px}
.nav a.active{color:var(--red)}
.hero h1{position:absolute;left:111px;top:142px;width:480px;font-size:42px;line-height:52px;font-weight:600;color:var(--white)}
.hero h1 span{color:var(--red)}
.hero p{position:absolute;left:111px;top:264px;width:460px;font-size:14px;line-height:26px;color:var(--white)}
.btn{display:inline-block;background:var(--red);color:var(--white);font-size:15px;font-weight:600;
  border-radius:26px;text-align:center;text-decoration:none}
.hero .btn{position:absolute;left:111px;top:339px;width:148px;height:50px;line-height:50px}
.thumb{position:absolute;top:480px;height:163px}
.thumb-caption{position:absolute;left:26px;bottom:24px;color:var(--white);font-family:"Poppins",sans-serif;font-size:15px}
.play{position:absolute;right:22px;bottom:14px}
.slider-arrow{position:absolute;top:545px;width:32px;height:32px;border-radius:50%;background:var(--white);
  display:flex;align-items:center;justify-content:center}

/* events */
.section-title{position:absolute;left:0;width:1200px;text-align:center;font-size:35px;font-weight:500;color:var(--ink)}
.event-card{position:absolute;width:312px;height:441px;background:var(--white);box-shadow:0 2px 12px rgba(0,0,0,.12)}
.event-card .photo{width:312px;height:245px}
.date{position:absolute;left:12px;top:265px;width:66px;height:69px;background:var(--red);color:var(--white);
  text-align:center;font-family:"Poppins",sans-serif}
.date .m{font-size:20px;line-height:28px;display:block;padding-top:2px}
.date .d{font-size:32px;line-height:34px;display:block;font-weight:500}
.event-card h3{position:absolute;left:100px;top:262px;width:200px;font-size:25px;line-height:35px;font-weight:500;color:var(--ink)}
.event-card p{position:absolute;left:100px;top:340px;width:200px;font-size:14px;line-height:26px;color:var(--muted)}
.more{position:absolute;left:100px;top:384px;font-family:"Poppins",sans-serif;font-size:15px;color:var(--red);text-decoration:underline}

/* blog */
.blog-panel{position:absolute;left:0;top:1906px;width:586px;height:599px;background:var(--grey)}
.blog-title{position:absolute;left:111px;top:2026px;font-size:36px;font-weight:500;color:var(--ink)}
.blog-title span,.about h2 span{color:var(--red)}
.blog-intro{position:absolute;left:111px;top:2089px;width:315px;font-size:15px;line-height:26.6px;color:var(--text)}
.pager{position:absolute;top:2330px}
.blog-post{position:absolute;top:1996px}
.blog-post .photo{height:351px}
.blog-post h4{font-size:23px;font-weight:500;color:var(--ink);margin-top:14px;line-height:30px}
.blog-post small{display:block;font-size:15px;color:#aaaaaa;margin-top:2px}

/* about */
.about-card{position:absolute;left:547px;top:2706px;width:539px;height:446px;background:var(--grey)}
.about h2{position:absolute;left:587px;top:2730px;font-size:36px;font-weight:500;color:var(--ink)}
.about p{position:absolute;left:587px;top:2798px;width:470px;font-size:14.5px;line-height:26.6px}
.about .btn{position:absolute;left:587px;top:3065px;width:149px;height:51px;line-height:51px}

/* newsletter */
.newsletter{position:absolute;left:0;top:3241px;width:1200px;height:249px;
  background:linear-gradient(90deg,var(--red),var(--coral) 60%,#e8574a)}
.newsletter h2{position:absolute;left:111px;top:60px;font-size:38px;font-weight:600;color:var(--white)}
.newsletter p{position:absolute;left:111px;top:119px;width:450px;font-size:15px;line-height:24px;color:var(--white)}
.email{position:absolute;left:605px;top:64px;width:482px;height:54px;border:1px solid var(--white);border-radius:27px;
  color:var(--white);font-size:15px;line-height:52px;padding-left:34px}
.subscribe{position:absolute;left:611px;top:138px;width:140px;height:51px;border-radius:26px;background:var(--white);
  color:var(--red);font-family:"Poppins",sans-serif;font-size:15px;font-weight:500;text-align:center;line-height:51px}

/* footer */
.footer{position:absolute;left:0;top:3490px;width:1200px;height:378px;background:var(--ink);color:var(--white)}
.footer .brand{left:146px;top:72px;font-size:28px}
.footer .about-text{position:absolute;left:146px;top:123px;width:260px;font-size:15px;line-height:26px}
.footer h4{position:absolute;top:68px;font-size:25px;font-weight:500}
.footer ul{position:absolute;top:117px;list-style:none;font-size:15px;line-height:27px}
.footer hr{position:absolute;left:146px;top:278px;width:940px;border:0;border-top:1px solid #2a2a2a}
.copyright{position:absolute;left:0;top:314px;width:1200px;text-align:center;font-size:15px}
</style>
</head>
<body>

<header class="hero">
  <div class="hero-shade" role="img" aria-label="Photo of a ballet teacher and a young girl dancing in a bright studio"></div>
  <div class="brand">Studio Pirouette</div>
  <nav class="nav">
    <a class="active" style="left:536px">Home</a>
    <a style="left:632px">About Us</a>
    <a style="left:754px">Our Videos</a>
    <a style="left:890px">Our Blog</a>
    <a style="left:1009px">Contact Us</a>
  </nav>
  <h1>Welcome To <span>Studio Pirouette</span></h1>
  <p>Lorem ipsum dolor sit amet, consectetur adipiscing elit, sed do eiusmod tempor incididunt ut labore</p>
  <a class="btn">Learn More</a>

  <div class="thumb" style="left:111px;width:264px;background:linear-gradient(135deg,#eef0f2,#b9c3d3 60%,#5a6f9a)" role="img" aria-label="Photo of a mother and daughter stretching on the floor"></div>
  <div class="thumb" style="left:386px;width:264px;background:linear-gradient(135deg,#a2171c,#6c1015 60%,#4a2a2a)" role="img" aria-label="Video still of a girl dancing on a red stage">
    <span class="thumb-caption">Lorem Ipsum</span>
    <svg class="play" width="36" height="36" viewBox="0 0 36 36"><circle cx="18" cy="18" r="18" fill="#EB3D1F"/><path d="M14 11 L25 18 L14 25 Z" fill="#fff"/></svg>
  </div>
  <div class="thumb" style="left:662px;width:264px;background:linear-gradient(135deg,#f4f4f2,#dcd6cf 60%,#e9c9cc)" role="img" aria-label="Photo of a teacher guiding a little ballerina"></div>
  <div class="thumb" style="left:931px;width:269px;background:linear-gradient(90deg,#7a6a5a,#3a3030 55%,#d3a33a)" role="img" aria-label="Photo of a mother hugging her dancer daughter"></div>

  <div class="slider-arrow" style="left:40px"><svg width="10" height="10" viewBox="0 0 10 10"><path d="M6.5 1.5 L3 5 L6.5 8.5" stroke="#333" stroke-width="1.4" fill="none"/></svg></div>
  <div class="slider-arrow" style="left:1131px"><svg width="10" height="10" viewBox="0 0 10 10"><path d="M3.5 1.5 L7 5 L3.5 8.5" stroke="#333" stroke-width="1.4" fill="none"/></svg></div>
</header>

<main>
  <h2 class="section-title" style="top:800px">UpComing Event</h2>

  <article class="event-card" style="left:111px;top:908px">
    <div class="photo" style="background:linear-gradient(135deg,#f3f3f3,#d9d9d9 50%,#9a9a9a)" role="img" aria-label="Photo of a teacher and girl practising a stretch"></div>
    <div class="date"><span class="m">Nov</span><span class="d">11</span></div>
    <h3>Lorem ipsum dolor sit</h3>
    <p>Lorem ipsum dolor sit amet consectetur adipiscing elit</p>
    <a class="more">Learn More</a>
  </article>
  <article class="event-card" style="left:443px;top:908px">
    <div class="photo" style="background:linear-gradient(180deg,#e8e8e8,#bdbdbd 55%,#2a2a2a)" role="img" aria-label="Photo of a dancer in an arabesque before a seated class"></div>
    <div class="date"><span class="m">Nov</span><span class="d">11</span></div>
    <h3>Lorem ipsum dolor sit</h3>
    <p>Lorem ipsum dolor sit amet consectetur adipiscing elit</p>
    <a class="more">Learn More</a>
  </article>
  <article class="event-card" style="left:773px;top:908px">
    <div class="photo" style="background:linear-gradient(180deg,#b9aca0,#6d6058 60%,#3d3532)" role="img" aria-label="Photo of young ballet students resting in a studio"></div>
    <div class="date"><span class="m">Nov</span><span class="d">11</span></div>
    <h3>Lorem ipsum dolor sit</h3>
    <p>Lorem ipsum dolor sit amet consectetur adipiscing elit</p>
    <a class="more">Learn More</a>
  </article>

  <article class="event-card" style="left:111px;top:1379px">
    <div class="photo" style="background:linear-gradient(135deg,#f0f0f0,#c9d3d6 50%,#4a4a4a)" role="img" aria-label="Photo of a group of women in a dance class"></div>
    <div class="date"><span class="m">Nov</span><span class="d">11</span></div>
    <h3>Lorem ipsum dolor sit</h3>
    <p>Lorem ipsum dolor sit amet consectetur adipiscing elit</p>
    <a class="more">Learn More</a>
  </article>
  <article class="event-card" style="left:443px;top:1379px">
    <div class="photo" style="background:linear-gradient(135deg,#6e5a4a,#b7a08c 50%,#8d8d8d)" role="img" aria-label="Photo of a mother and daughter stretching together"></div>
    <div class="date"><span class="m">Nov</span><span class="d">11</span></div>
    <h3>Lorem ipsum dolor sit</h3>
    <p>Lorem ipsum dolor sit amet consectetur adipiscing elit</p>
    <a class="more">Learn More</a>
  </article>
  <article class="event-card" style="left:773px;top:1379px">
    <div class="photo" style="background:linear-gradient(180deg,#dfe4e8,#c3c9cf 60%,#a9a2a6)" role="img" aria-label="Photo of a children's ballet class raising their arms"></div>
    <div class="date"><span class="m">Nov</span><span class="d">11</span></div>
    <h3>Lorem ipsum dolor sit</h3>
    <p>Lorem ipsum dolor sit amet consectetur adipiscing elit</p>
    <a class="more">Learn More</a>
  </article>

  <section class="blog">
    <div class="blog-panel"></div>
    <h2 class="blog-title">Our <span>Blog</span></h2>
    <p class="blog-intro">Lorem ipsum dolor sit amet, consectetur adipiscing elit, sed do eiusmod tempor incididunt ut labore et dolore magna aliqua. Quis ipsum suspendisse ultrices gravida. Risus commodo viverra maecenas accumsan lacus vel facilisis. Lorem ipsum dolor sit amet, consectetur adipiscing elit, sed do eiusmod tempor</p>
    <svg class="pager" style="left:111px" width="46" height="46" viewBox="0 0 46 46"><path d="M1 1 L40 1 L45 45 L1 45 Z" fill="none" stroke="#888" stroke-width="1.5"/><path d="M24 19 L20 23 L24 27" stroke="#333" stroke-width="1.5" fill="none"/></svg>
    <svg class="pager" style="left:168px" width="46" height="46" viewBox="0 0 46 46"><path d="M10 1 L45 1 L45 45 L1 45 Z" fill="none" stroke="#888" stroke-width="1.5"/><path d="M22 19 L26 23 L22 27" stroke="#333" stroke-width="1.5" fill="none"/></svg>

    <div class="blog-post" style="left:458px;width:254px">
      <div class="photo" style="background:linear-gradient(180deg,#e9edf1,#c7ccd2 60%,#8a8f96)" role="img" aria-label="Photo of a smiling mother and daughter stretching"></div>
      <h4>Lorem Ipsum</h4><small>Lorem Ipsum</small>
    </div>
    <div class="blog-post" style="left:727px;width:255px">
      <div class="photo" style="background:linear-gradient(180deg,#5d5f61,#3f4042 60%,#6b5a4c)" role="img" aria-label="Photo of a young dancer with her mother and a small dog"></div>
      <h4>Lorem Ipsum</h4><small>Lorem Ipsum</small>
    </div>
    <div class="blog-post" style="left:997px;width:203px">
      <div class="photo" style="background:linear-gradient(135deg,#d8d2cc,#8e7e72 55%,#2a2524)" role="img" aria-label="Photo of a teacher helping a girl at the barre"></div>
      <h4>Lorem Ipsum</h4><small>Lorem Ipsum</small>
    </div>
  </section>

  <section class="about">
    <div class="abs" style="left:111px;top:2598px;width:601px;height:480px;background:linear-gradient(100deg,#b89a86,#d7c9bd 45%,#8f7a6c)" role="img" aria-label="Photo of a girl and a teacher dancing in a brick-walled studio"></div>
    <div class="about-card"></div>
    <h2>About <span>Studio Pirouette</span></h2>
    <p>Lorem ipsum dolor sit amet, consectetur adipiscing elit, sed do eiusmod tempor incididunt ut labore et dolore magna aliqua. Quis ipsum suspendisse ultrices gravida. Risus commodo viverra maecenas accumsan lacus vel facilisis. Lorem ipsum dolor sit amet, consectetur adipiscing elit, sed do eiusmod tempor incididunt ut labore et dolore magna aliqua. Quis ipsum suspendisse ultrices gravida. Risus commodo viverra maecenas accumsan lacus vel facilisis. Lorem ipsum dolor sit amet, consectetur adipiscing elit, sed do eiusmod</p>
    <a class="btn">Learn More</a>
  </section>

  <section class="newsletter">
    <h2>Subscribe to Newsletter</h2>
    <p>Lorem ipsum dolor sit amet, consectetur adipiscing elit, sed do eiusmod tempor</p>
    <div class="email">Your Email Address</div>
    <div class="subscribe">SUBSCRIBE</div>
  </section>
</main>

<footer class="footer">
  <div class="brand">Studio Pirouette</div>
  <p class="about-text">Lorem ipsum dolor sit amet, consectetur adipiscing elit, sed do eiusmod tempor incididunt</p>
  <h4 style="left:497px">Quick Link</h4>
  <ul style="left:498px"><li>Home</li><li>About Us</li><li>Our Videos</li><li>Our Blog</li><li>Contact Us</li></ul>
  <h4 style="left:716px">Company</h4>
  <ul style="left:718px"><li>About Us</li><li>Team</li></ul>
  <h4 style="left:923px">Help Link</h4>
  <ul style="left:925px"><li>Terms&amp;condtions</li><li>Privacy Policy</li><li>About Us</li><li>Support</li></ul>
  <hr>
  <p class="copyright">©Copyrights 2021 Company Name &nbsp;| &nbsp; All Rights Reserved</p>
</footer>

</body>
</html>
```